BrookhavenLLC

Real Estate Investment. Buy/Sell house/investment . Trustworthy,Reliable, and friendly

Industry/Entity Type

Real Estate

Contact Information for Business Card

Brookhaven@mailbox-example.com
808-555-0143
Linnea-Joy Patterson

```html
<!DOCTYPE html>
<html lang="en">
<head>
<meta charset="utf-8">
<title>BrookhavenLLC — Business Card</title>
<link rel="stylesheet" href="https://fonts.googleapis.com/css2?family=Montserrat:wght@400;500;600;700&display=swap">
<style>
  :root {
    --navy-deep: #061320;
    --navy: #0a2233;
    --teal-glow: #0f4a55;
    --white: #ffffff;
    --ink: #0b1a26;
    --bar-green: #0b7a44;
    --bar-teal: #0aa0b0;
    --bar-blue: #0a73bd;
    --icon-green: #117a45;
  }
  * { margin: 0; padding: 0; box-sizing: border-box; }
  html, body {
    width: 1200px; height: 702px; overflow: hidden;
    background: var(--navy-deep);
  }
  .card {
    position: relative;
    width: 1200px; height: 702px; overflow: hidden;
    font-family: "Montserrat", sans-serif;
    background:
      radial-gradient(ellipse 520px 360px at 720px 250px, var(--teal-glow) 0%, rgba(15,74,85,0) 100%),
      radial-gradient(ellipse 700px 500px at 300px 150px, #0b2b3c 0%, rgba(11,43,60,0) 100%),
      linear-gradient(160deg, var(--navy) 0%, var(--navy-deep) 100%);
  }
  .backdrop-texture {
    position: absolute; inset: 0;
    background: linear-gradient(200deg, rgba(255,255,255,0.03) 0%, rgba(0,0,0,0.15) 100%);
  }
  .accent-bars { position: absolute; display: flex; height: 20px; }
  .accent-bars span { display: block; width: 219px; height: 100%; }
  .accent-bars--top { top: 0; left: 544px; }
  .accent-bars--bottom { bottom: 0; left: 0; height: 19px; }
  .bar-green { background: var(--bar-green); }
  .bar-teal { background: var(--bar-teal); }
  .bar-blue { background: var(--bar-blue); }

  .company-name {
    position: absolute; left: 356px; top: 205px;
    font-weight: 700; font-size: 88px; line-height: 1;
    color: var(--white); letter-spacing: 0.5px;
  }
  .email-band {
    position: absolute; left: 310px; top: 288px;
    width: 900px; height: 68px;
    background: var(--white);
    border-radius: 34px 0 0 34px;
    display: flex; align-items: center;
    padding-left: 54px;
  }
  .email {
    font-weight: 400; font-size: 31px;
    color: var(--ink); letter-spacing: 4px;
  }
  .person-name {
    position: absolute; left: 504px; top: 400px;
    font-weight: 600; font-size: 39px; line-height: 1;
    color: var(--white); letter-spacing: 5px;
  }
  .phone {
    position: absolute; left: 491px; top: 445px;
    display: flex; align-items: center;
  }
  .phone-icon { width: 46px; height: 46px; flex: none; }
  .phone-number {
    margin-left: 6px;
    font-weight: 500; font-size: 31px;
    color: var(--white); letter-spacing: 4px;
  }
</style>
</head>
<body>
<div class="card">
  <div class="backdrop-texture" role="img" aria-label="Soft abstract backdrop of overlapping dark teal curves"></div>

  <div class="accent-bars accent-bars--top">
    <span class="bar-green"></span><span class="bar-teal"></span><span class="bar-blue"></span>
  </div>

  <h1 class="company-name">BrookhavenLLC</h1>

  <div class="email-band">
    <span class="email">Brookhaven@mailbox-example.com</span>
  </div>

  <p class="person-name">Linnea-Joy Patterson</p>

  <div class="phone">
    <svg class="phone-icon" viewBox="0 0 46 46" aria-hidden="true">
      <circle cx="23" cy="23" r="23" fill="var(--icon-green)"/>
      <path d="M16 12c1-1 2.4-1 3.2 0l2.6 3.4c.7.9.6 2.1-.2 2.9l-1.6 1.6c1.2 2.6 3.4 4.8 6 6l1.6-1.6c.8-.8 2-.9 2.9-.2l3.4 2.6c1 .8 1 2.2 0 3.2l-1.8 1.8c-1.6 1.6-4.2 1.8-6.2.5-4.2-2.8-7.9-6.5-10.7-10.7-1.3-2-1.1-4.6.5-6.2z"
            fill="none" stroke="var(--white)" stroke-width="2" stroke-linejoin="round"/>
    </svg>
    <span class="phone-number">808-555-0143</span>
  </div>

  <div class="accent-bars accent-bars--bottom">
    <span class="bar-blue"></span><span class="bar-teal"></span><span class="bar-green"></span>
  </div>
</div>
</body>
</html>
```